Wirenexa

I'm looking to much improve our current website wirenexa.com
Updates

Low design quality

Target Market(s)

Commercial clients (Not-Residentials)

Industry/Entity Type

Office buildings and Industrial clients

Coding

Coded - Design and coding required

Number of Pages Required

5+ page

Requirements
Must have
• Very professional structured low voltage cabling projects for Wi-Fi, Audio/Video conference rooms, Access Control systems, CCTV.

```html
<!DOCTYPE html>
<html lang="en">
<head>
<meta charset="utf-8">
<title>Contact – Wirenexa</title>
<link href="https://fonts.googleapis.com/css2?family=Inter:wght@400;500;600;700&family=Rajdhani:wght@600;700&display=swap" rel="stylesheet">
<style>
:root{
  --red:#e0283e;
  --red-dark:#c8182f;
  --ink:#1a1416;
  --hero:#110b0c;
  --strip:#1c1314;
  --main:#0d0a0a;
  --card:#180f11;
  --card-line:#2e1e21;
  --area:#1c1215;
  --cta:#f7eeef;
  --foot:#f9f6f6;
  --muted:#9b8f91;
  --light:#f3eded;
  --head:"Rajdhani",sans-serif;
  --body:"Inter",sans-serif;
}
*{box-sizing:border-box;margin:0;padding:0}
html,body{width:1200px;height:2267px;overflow:hidden}
body{font-family:var(--body);background:var(--main);color:var(--light);position:relative}
section,header,footer{position:absolute;left:0;width:1200px}
.abs{position:absolute}
svg{display:block}

/* nav */
.nav{top:0;height:63px;background:#efeeee;border-bottom:1px solid #dcd6d6}
.logo{font-family:var(--head);font-weight:700;font-size:27px;color:var(--ink);display:flex;align-items:center;gap:6px}
.logo .mark{width:18px;height:18px;background:var(--red)}
.nav .logo{left:104px;top:16px}
.nav-links{left:513px;top:23px;display:flex;gap:29px;font-size:13px;font-weight:500;color:var(--ink)}
.nav-links .active{color:var(--red);border-bottom:2px solid var(--red);padding-bottom:5px}
.nav-phone{left:884px;top:23px;font-size:13px;font-weight:500;color:var(--ink);display:flex;gap:6px;align-items:center}
.btn-red{background:var(--red);color:#fff;font-weight:600;border-radius:4px;display:flex;align-items:center;justify-content:center;box-shadow:0 4px 12px rgba(224,40,62,.3)}
.nav .btn-red{left:997px;top:15px;width:99px;height:33px;font-size:12px}

/* hero */
.hero{top:63px;height:362px;background:radial-gradient(circle at 22% 10%,#3a1014 0,#1a0d0f 30%,var(--hero) 60%);text-align:center}
.pill{left:527px;top:71px;width:146px;height:27px;border:1px solid #5a1d25;border-radius:14px;background:#2a1115;color:var(--red);font-size:10px;font-weight:700;letter-spacing:2px;display:flex;align-items:center;justify-content:center;gap:7px}
.hero h1{position:absolute;top:115px;width:100%;font-family:var(--head);font-size:50px;font-weight:700;color:#fff}
.hero h1 span,.accent{color:var(--red)}
.hero p{position:absolute;top:194px;left:340px;width:520px;font-size:15px;line-height:23px;color:#c9bfc1}
.crumb{position:absolute;top:262px;width:100%;font-size:11px;color:#7a6e70}
.crumb b{color:#d8d0d1;font-weight:400}

/* strip */
.strip{top:425px;height:87px;background:var(--strip);border-top:1px solid #2a1c1e}
.strip-item{top:23px;display:flex;gap:14px;align-items:center}
.ibox{width:40px;height:40px;border-radius:6px;background:#2b1418;border:1px solid #4a1c23;display:flex;align-items:center;justify-content:center}
.kicker{font-size:10px;letter-spacing:1.3px;color:#8c7f81;font-weight:600}
.strip-item strong{display:block;font-size:14px;font-weight:600;color:#fff;margin-top:4px}
.divider{top:20px;width:1px;height:46px;background:#33272a}

/* main */
.main{top:512px;height:843px;background:var(--main)}
.form-card{left:104px;top:84px;width:511px;height:668px;background:var(--card);border:1px solid var(--card-line);border-radius:12px}
.form-card h2{position:absolute;left:33px;top:37px;font-family:var(--head);font-size:23px;font-weight:700;color:#fff}
.form-card .intro{position:absolute;left:33px;top:79px;width:440px;font-size:12px;line-height:19px;color:#b9adaf}
.label{font-size:12px;font-weight:500;color:#d9d0d1}
.field{height:37px;border:1px solid #2d1e21;border-radius:4px;background:#130c0e;font-size:13px;color:#6f6264;padding:10px 14px}
.select{height:38px;border:1px solid #3a2a2d;background:#0f0a0b;color:#f1eaea;font-size:13px;padding:10px 17px;display:flex;justify-content:space-between;align-items:center;border-radius:4px}
.send{left:33px;top:590px;width:444px;height:43px;font-size:14px;border-radius:4px;gap:8px;background:linear-gradient(90deg,var(--red-dark),#ee3d54)}

.offices-title{left:670px;top:88px;font-family:var(--head);font-size:23px;font-weight:700;color:#fff}
.ocard{left:670px;width:426px;background:var(--card);border:1px solid var(--card-line);border-radius:10px}
.ohead{position:absolute;left:20px;top:20px;display:flex;gap:16px;align-items:center}
.ohead .kicker{color:var(--red);font-weight:700}
.ohead h3{font-family:var(--head);font-size:15px;font-weight:700;color:#fff;margin-top:3px}
.oline{position:absolute;left:20px;right:20px;height:1px;background:#2d1e21}
.orow{position:absolute;left:20px;display:flex;gap:10px;font-size:12px;line-height:19px;color:#cfc5c6}
.orow svg{margin-top:3px;flex:none}
.hours-row{position:absolute;left:20px;right:20px;display:flex;justify-content:space-between;font-size:12px;color:#a99d9f}
.hours-row b{color:#fff;font-weight:600}

/* service area */
.area{top:1355px;height:381px;background:var(--area);text-align:center}
.area .kicker{position:absolute;top:94px;width:100%;color:var(--red);font-weight:700;font-size:10px;letter-spacing:2px}
.area .kicker::before{content:"";display:inline-block;width:20px;height:1px;background:var(--red);vertical-align:middle;margin-right:8px}
.area h2{position:absolute;top:120px;width:100%;font-family:var(--head);font-size:40px;font-weight:700;color:#fff}
.area p{position:absolute;top:180px;left:360px;width:480px;font-size:14.5px;line-height:24px;color:#b7abad}
.tags{position:absolute;top:262px;left:0;width:100%;display:flex;justify-content:center;gap:9px}
.tag{height:37px;padding:0 17px;border:1px solid #5a1d25;border-radius:19px;background:#2a1216;color:var(--red);font-size:12px;font-weight:500;display:flex;align-items:center}

/* cta */
.cta{top:1736px;height:144px;background:var(--cta);border-bottom:1px solid #eadada}
.cta h2{position:absolute;left:104px;top:45px;font-family:var(--head);font-size:22px;font-weight:700;color:var(--ink)}
.cta p{position:absolute;left:104px;top:85px;font-size:14px;color:#5d5153}
.btn-out{left:781px;top:51px;width:158px;height:44px;border:1px solid #d6c9ca;background:#fff;border-radius:4px;font-size:14px;color:var(--ink);display:flex;align-items:center;justify-content:center;gap:8px}
.cta .btn-red{left:950px;top:51px;width:146px;height:44px;font-size:13.5px}

/* footer */
.foot{top:1880px;height:387px;background:var(--foot)}
.foot .logo{left:104px;top:60px;font-size:25px}
.foot .about{left:104px;top:120px;width:285px;font-size:12px;line-height:20px;color:#6a5e60}
.social{left:104px;top:196px;display:flex;gap:9px}
.social span{width:29px;height:29px;border:1px solid #e2d8d9;background:#fff;border-radius:4px;display:flex;align-items:center;justify-content:center}
.social span i{width:9px;height:9px;background:#c9bcbe}
.fcol h4{font-family:var(--head);font-size:12.5px;letter-spacing:1.5px;color:var(--ink);font-weight:700;padding-bottom:12px;border-bottom:1px solid #e6dcdd}
.fcol ul{list-style:none;padding-left:15px;margin-top:10px}
.fcol li{font-size:12px;color:#3e3335;line-height:27px}
.fc{display:flex;gap:10px;font-size:11.5px;line-height:17px;color:#3e3335;margin-top:13px}
.fc svg{margin-top:2px;flex:none}
.fc b{font-weight:600;letter-spacing:.5px}
.bottom{left:0;top:336px;width:1200px;height:1px;background:#e6dcdd}
.copy{top:353px;font-size:10.5px;color:#6a5e60}
</style>
</head>
<body>

<header class="nav">
  <div class="abs logo"><span class="mark"></span>Wirenexa</div>
  <nav class="abs nav-links"><span>Home</span><span>About</span><span>Services</span><span>Projects</span><span class="active">Contact</span></nav>
  <div class="abs nav-phone"><svg width="12" height="12" viewBox="0 0 24 24" fill="none" stroke="#1a1416" stroke-width="2"><path d="M22 16.9v3a2 2 0 0 1-2.2 2 19.8 19.8 0 0 1-8.6-3.1 19.5 19.5 0 0 1-6-6A19.8 19.8 0 0 1 2.1 4.2 2 2 0 0 1 4.1 2h3a2 2 0 0 1 2 1.7c.1 1 .4 1.9.7 2.8a2 2 0 0 1-.5 2.1L8 9.9a16 16 0 0 0 6 6l1.3-1.3a2 2 0 0 1 2.1-.4c.9.3 1.8.6 2.8.7a2 2 0 0 1 1.7 2z"/></svg>888-555-0147</div>
  <div class="abs btn-red">Get a Quote</div>
</header>

<section class="hero">
  <div class="abs pill"><svg width="10" height="10" viewBox="0 0 24 24" fill="#e0283e"><path d="M22 16.9v3a2 2 0 0 1-2.2 2 19.8 19.8 0 0 1-8.6-3.1 19.5 19.5 0 0 1-6-6A19.8 19.8 0 0 1 2.1 4.2 2 2 0 0 1 4.1 2h3a2 2 0 0 1 2 1.7c.1 1 .4 1.9.7 2.8a2 2 0 0 1-.5 2.1L8 9.9a16 16 0 0 0 6 6l1.3-1.3a2 2 0 0 1 2.1-.4c.9.3 1.8.6 2.8.7a2 2 0 0 1 1.7 2z"/></svg>GET IN TOUCH</div>
  <h1>Let's <span>Connect</span></h1>
  <p>Ready to start your project? Contact our team for a free consultation and discover how Wirenexa can elevate your IT infrastructure.</p>
  <div class="crumb">Home &nbsp;/&nbsp; <b>Contact</b></div>
</section>

<section class="strip">
  <div class="abs strip-item" style="left:136px">
    <div class="ibox"><svg width="16" height="16" viewBox="0 0 24 24" fill="none" stroke="#e0283e" stroke-width="2"><path d="M22 16.9v3a2 2 0 0 1-2.2 2 19.8 19.8 0 0 1-8.6-3.1 19.5 19.5 0 0 1-6-6A19.8 19.8 0 0 1 2.1 4.2 2 2 0 0 1 4.1 2h3a2 2 0 0 1 2 1.7c.1 1 .4 1.9.7 2.8a2 2 0 0 1-.5 2.1L8 9.9a16 16 0 0 0 6 6l1.3-1.3a2 2 0 0 1 2.1-.4c.9.3 1.8.6 2.8.7a2 2 0 0 1 1.7 2z"/></svg></div>
    <div><div class="kicker">CALL US</div><strong>888-555-0147</strong></div>
  </div>
  <div class="abs divider" style="left:434px"></div>
  <div class="abs strip-item" style="left:468px">
    <div class="ibox"><svg width="16" height="16" viewBox="0 0 24 24" fill="none" stroke="#e0283e" stroke-width="2"><rect x="3" y="5" width="18" height="14" rx="2"/><path d="M3 7l9 6 9-6"/></svg></div>
    <div><div class="kicker">EMAIL US</div><strong>sales@wirenexa.com</strong></div>
  </div>
  <div class="abs divider" style="left:765px"></div>
  <div class="abs strip-item" style="left:799px">
    <div class="ibox"><svg width="16" height="16" viewBox="0 0 24 24" fill="none" stroke="#e0283e" stroke-width="2"><path d="M12 22s7-6.5 7-12a7 7 0 0 0-14 0c0 5.5 7 12 7 12z"/><circle cx="12" cy="10" r="2.5"/></svg></div>
    <div><div class="kicker">MAIN OFFICE</div><strong>Vienna, VA 22180</strong></div>
  </div>
</section>

<section class="main">
  <div class="abs form-card">
    <h2>Send Us a Message</h2>
    <p class="intro">Fill out the form below and a member of our team will get back to you within 24 hours.</p>
    <div class="abs label" style="left:33px;top:143px">First Name *</div>
    <div class="abs field" style="left:33px;top:162px;width:216px">John</div>
    <div class="abs label" style="left:262px;top:143px">Last Name *</div>
    <div class="abs field" style="left:262px;top:162px;width:215px">Smith</div>
    <div class="abs label" style="left:33px;top:217px">Email Address *</div>
    <div class="abs field" style="left:33px;top:236px;width:216px">john@company.com</div>
    <div class="abs label" style="left:262px;top:217px">Phone Number</div>
    <div class="abs field" style="left:262px;top:236px;width:215px">(555) 555-5555</div>
    <div class="abs label" style="left:33px;top:292px">Company Name</div>
    <div class="abs field" style="left:33px;top:311px;width:444px">Your Company</div>
    <div class="abs label" style="left:33px;top:367px">Service of Interest</div>
    <div class="abs select" style="left:33px;top:386px;width:444px">Select a service...<svg width="10" height="10" viewBox="0 0 24 24" fill="none" stroke="#f1eaea" stroke-width="3"><path d="M6 9l6 6 6-6"/></svg></div>
    <div class="abs label" style="left:33px;top:443px">Message *</div>
    <div class="abs field" style="left:33px;top:462px;width:444px;height:108px">Tell us about your project...</div>
    <div class="abs btn-red send"><svg width="14" height="14" viewBox="0 0 24 24" fill="none" stroke="#fff" stroke-width="2"><path d="M22 2L11 13M22 2l-7 20-4-9-9-4z"/></svg>Send Message</div>
  </div>

  <h2 class="abs offices-title">Our Offices</h2>

  <div class="abs ocard" style="top:141px;height:223px">
    <div class="ohead"><svg width="22" height="22" viewBox="0 0 24 24" fill="none" stroke="#8fb6d8" stroke-width="1.8"><rect x="5" y="3" width="14" height="18"/><path d="M9 7h2M13 7h2M9 11h2M13 11h2M9 15h2M13 15h2"/></svg><div><div class="kicker">MAIN OFFICE</div><h3>Virginia</h3></div></div>
    <div class="oline" style="top:73px"></div>
    <div class="orow" style="top:93px"><svg width="12" height="12" viewBox="0 0 24 24" fill="none" stroke="#e0283e" stroke-width="2"><path d="M12 22s7-6.5 7-12a7 7 0 0 0-14 0c0 5.5 7 12 7 12z"/><circle cx="12" cy="10" r="2.5"/></svg><div>4410 Linden Park Blvd, Suite 250<br>Vienna, VA 22180</div></div>
    <div class="orow" style="top:139px"><svg width="12" height="12" viewBox="0 0 24 24" fill="none" stroke="#e0283e" stroke-width="2"><path d="M22 16.9v3a2 2 0 0 1-2.2 2 19.8 19.8 0 0 1-8.6-3.1 19.5 19.5 0 0 1-6-6A19.8 19.8 0 0 1 2.1 4.2 2 2 0 0 1 4.1 2h3a2 2 0 0 1 2 1.7c.1 1 .4 1.9.7 2.8a2 2 0 0 1-.5 2.1L8 9.9a16 16 0 0 0 6 6l1.3-1.3a2 2 0 0 1 2.1-.4c.9.3 1.8.6 2.8.7a2 2 0 0 1 1.7 2z"/></svg><div>888-555-0147 (National)<br>703-555-0192 (Local)</div></div>
    <div class="orow" style="top:186px"><svg width="12" height="12" viewBox="0 0 24 24" fill="none" stroke="#e0283e" stroke-width="2"><rect x="3" y="5" width="18" height="14" rx="2"/><path d="M3 7l9 6 9-6"/></svg><div>sales@wirenexa.com</div></div>
  </div>

  <div class="abs ocard" style="top:381px;height:205px">
    <div class="ohead"><svg width="22" height="22" viewBox="0 0 24 24"><circle cx="12" cy="8" r="5" fill="#e0283e"/><path d="M12 13v9" stroke="#bbb" stroke-width="1.6"/></svg><div><div class="kicker">REGIONAL OFFICE</div><h3>Maryland</h3></div></div>
    <div class="oline" style="top:74px"></div>
    <div class="orow" style="top:94px"><svg width="12" height="12" viewBox="0 0 24 24" fill="none" stroke="#e0283e" stroke-width="2"><path d="M12 22s7-6.5 7-12a7 7 0 0 0-14 0c0 5.5 7 12 7 12z"/><circle cx="12" cy="10" r="2.5"/></svg><div>5820 Harbor Ridge Drive, Suite 400<br>Bethesda, MD 20814</div></div>
    <div class="orow" style="top:140px"><svg width="12" height="12" viewBox="0 0 24 24" fill="none" stroke="#e0283e" stroke-width="2"><path d="M22 16.9v3a2 2 0 0 1-2.2 2 19.8 19.8 0 0 1-8.6-3.1 19.5 19.5 0 0 1-6-6A19.8 19.8 0 0 1 2.1 4.2 2 2 0 0 1 4.1 2h3a2 2 0 0 1 2 1.7c.1 1 .4 1.9.7 2.8a2 2 0 0 1-.5 2.1L8 9.9a16 16 0 0 0 6 6l1.3-1.3a2 2 0 0 1 2.1-.4c.9.3 1.8.6 2.8.7a2 2 0 0 1 1.7 2z"/></svg><div>888-555-0147 (National)</div></div>
    <div class="orow" style="top:168px"><svg width="12" height="12" viewBox="0 0 24 24" fill="none" stroke="#e0283e" stroke-width="2"><rect x="3" y="5" width="18" height="14" rx="2"/><path d="M3 7l9 6 9-6"/></svg><div>sales@wirenexa.com</div></div>
  </div>

  <div class="abs ocard" style="top:603px;height:158px">
    <div class="abs" style="left:20px;top:23px;font-family:var(--head);font-size:13.5px;font-weight:700;color:#fff">Business Hours</div>
    <div class="oline" style="top:52px"></div>
    <div class="hours-row" style="top:68px"><span>Monday – Friday</span><b>8:00 AM – 6:00 PM</b></div>
    <div class="hours-row" style="top:95px"><span>Saturday</span><b>By Appointment</b></div>
    <div class="hours-row" style="top:122px"><span>Sunday</span><b>Closed</b></div>
  </div>
</section>

<section class="area">
  <div class="kicker">SERVICE AREA</div>
  <h2>Serving <span class="accent">Virginia · DC · Maryland</span> &amp; Nationwide</h2>
  <p>Primary service area covers the DC metro region, with national project capabilities.</p>
  <div class="tags"><span class="tag">Northern Virginia</span><span class="tag">Washington DC</span><span class="tag">Maryland</span><span class="tag">Nationwide Projects</span><span class="tag">Federal Facilities</span><span class="tag">Commercial Properties</span><span class="tag">Industrial Sites</span></div>
</section>

<section class="cta">
  <h2>Ready to Upgrade Your Infrastructure?</h2>
  <p>Let's build a smarter, more connected workspace together.</p>
  <div class="abs btn-out"><svg width="13" height="13" viewBox="0 0 24 24" fill="none" stroke="#1a1416" stroke-width="2"><path d="M22 16.9v3a2 2 0 0 1-2.2 2 19.8 19.8 0 0 1-8.6-3.1 19.5 19.5 0 0 1-6-6A19.8 19.8 0 0 1 2.1 4.2 2 2 0 0 1 4.1 2h3a2 2 0 0 1 2 1.7c.1 1 .4 1.9.7 2.8a2 2 0 0 1-.5 2.1L8 9.9a16 16 0 0 0 6 6l1.3-1.3a2 2 0 0 1 2.1-.4c.9.3 1.8.6 2.8.7a2 2 0 0 1 1.7 2z"/></svg>888-555-0147</div>
  <div class="abs btn-red">Request a Quote</div>
</section>

<footer class="foot">
  <div class="abs logo"><span class="mark"></span>Wirenexa</div>
  <p class="abs about">Leading infrastructure cabling company dedicated to building, managing, securing, and supporting IT infrastructure since 1994.</p>
  <div class="abs social"><span aria-label="Social profile"><i></i></span><span aria-label="Social profile"><i></i></span><span aria-label="Social profile"><i></i></span></div>

  <div class="abs fcol" style="left:422px;top:60px;width:175px">
    <h4>QUICK LINKS</h4>
    <ul><li>Home</li><li>About Us</li><li>Services</li><li>Projects</li><li>Contact</li><li>Get a Quote</li></ul>
  </div>
  <div class="abs fcol" style="left:637px;top:60px;width:175px">
    <h4>OUR SERVICES</h4>
    <ul><li>Structured Cabling</li><li>Wi-Fi Solutions</li><li>Audio/Video Systems</li><li>Access Control</li><li>CCTV &amp; Security</li><li>IDF/MDF &amp; Racking</li></ul>
  </div>
  <div class="abs fcol" style="left:852px;top:60px;width:244px">
    <h4>CONTACT US</h4>
    <div class="fc"><svg width="12" height="12" viewBox="0 0 24 24" fill="none" stroke="#e0283e" stroke-width="2"><path d="M12 22s7-6.5 7-12a7 7 0 0 0-14 0c0 5.5 7 12 7 12z"/><circle cx="12" cy="10" r="2.5"/></svg><div><b>MAIN OFFICE (VA)</b><br>4410 Linden Park Blvd, Suite 250<br>Vienna, VA 22180</div></div>
    <div class="fc"><svg width="12" height="12" viewBox="0 0 24 24" fill="none" stroke="#e0283e" stroke-width="2"><path d="M12 22s7-6.5 7-12a7 7 0 0 0-14 0c0 5.5 7 12 7 12z"/><circle cx="12" cy="10" r="2.5"/></svg><div><b>REGIONAL (MD)</b><br>5820 Harbor Ridge Drive, Suite 400<br>Bethesda, MD 20814</div></div>
    <div class="fc"><svg width="12" height="12" viewBox="0 0 24 24" fill="none" stroke="#e0283e" stroke-width="2"><path d="M22 16.9v3a2 2 0 0 1-2.2 2 19.8 19.8 0 0 1-8.6-3.1 19.5 19.5 0 0 1-6-6A19.8 19.8 0 0 1 2.1 4.2 2 2 0 0 1 4.1 2h3a2 2 0 0 1 2 1.7c.1 1 .4 1.9.7 2.8a2 2 0 0 1-.5 2.1L8 9.9a16 16 0 0 0 6 6l1.3-1.3a2 2 0 0 1 2.1-.4c.9.3 1.8.6 2.8.7a2 2 0 0 1 1.7 2z"/></svg><div>888-555-0147 (National)<br>703-555-0192 (Local)</div></div>
    <div class="fc"><svg width="12" height="12" viewBox="0 0 24 24" fill="none" stroke="#e0283e" stroke-width="2"><rect x="3" y="5" width="18" height="14" rx="2"/><path d="M3 7l9 6 9-6"/></svg><div>sales@wirenexa.com</div></div>
  </div>

  <div class="abs bottom"></div>
  <div class="abs copy" style="left:104px">© 2026 Wirenexa. All rights reserved.</div>
  <div class="abs copy" style="right:104px">Serving Virginia • Maryland • Washington DC &amp; Nationwide</div>
</footer>

</body>
</html>
```